Outdoor group fitness training - Greta Moxley Personal Training

I want an eye catching A4 flyer that promotes my two outdoor fitness groups. I have uploaded photos of each location: Mylor and Pasadena.
The target group is existing and potential new Personal training clients - all adults. There are two morning groups at Mylor ; one evening and one morning group at Pasadena. The groups will be for up to 8 people and are for all fitness levels.I want to encourage people to come and have a go. I have also uploaded a design I have used through printhollow for a previous flyer. I would like to use the orange graphic of the two people at the bottom of this design.
Cost is $15 per person
Location and times - Brackenridge Oval Wednesdays 7.30am; Sundays 8am
Corvale High School Thursdays 6.30pm: Saturdays 8am
Updates

Thanks so much to all of you for submitting a great set of designs. it was really hard making a choice in the end, and I really appreciate the promptness and creativity that went into the designs. I will certainly keep you in mind for future jobs. Cheers and have a great day Greta Moxley

Target Market(s)

40 - 60 year old adults: cross section of professionals, tradespeople and retirees. People who will enjoy socialising while also getting fit. No extremely fit people - cross section of beginners to intermediate; males and females

Industry/Entity Type

Training

Font styles to use
Sans Serif

Colors
f78f20
9bcb3c
ecf7fb

Requirements
Must have
• Fast turnaround required - within two days
Bright and attention grabbing, engaging. Could be A4 or could be postcard size?

State cost clearly
State that first 5 people to join either group will get first session at half price

```html
<!DOCTYPE html>
<html lang="en">
<head>
<meta charset="utf-8">
<title>Greta Moxley Personal Training – Outdoor Group Fitness</title>
<link href="https://fonts.googleapis.com/css2?family=Arimo:ital,wght@0,400;0,700;1,700&display=swap" rel="stylesheet">
<style>
  :root {
    --page-bg: #ecf7fb;
    --flyer-blue: #5f80b6;
    --orange: #f78f20;
    --green: #9bcb3c;
    --white: #ffffff;
    --ink: #111111;
    --night: #0a0a0c;
    --dusk-orange: #e2733a;
    --sky-mid: #8a93b3;
  }
  * { box-sizing: border-box; margin: 0; padding: 0; }
  html, body {
    width: 889px; height: 1200px; overflow: hidden;
    background: var(--page-bg);
    font-family: "Arimo", Arial, sans-serif;
  }
  .flyer {
    position: absolute; left: 127px; top: 150px;
    width: 636px; height: 900px;
    background: var(--flyer-blue);
    overflow: hidden;
  }
  .sunset-photo {
    position: absolute; left: 0; top: 450px; width: 636px; height: 410px;
    background: linear-gradient(180deg,
      var(--flyer-blue) 0%, #6e86b8 35%, var(--sky-mid) 60%,
      #b28a86 78%, var(--dusk-orange) 90%, #3a2420 97%, var(--night) 100%);
  }
  .client-name {
    position: absolute; left: 0; top: 42px; width: 636px;
    text-align: center; color: var(--white);
    font-weight: 700; font-style: italic; font-size: 80px; letter-spacing: 0.5px;
    line-height: 1;
  }
  .venue {
    position: absolute; left: 45px; width: 545px; height: 162px; display: flex;
  }
  .venue--corvale { top: 149px; }
  .venue--brackenridge { top: 326px; }
  .venue-photo { width: 289px; height: 162px; flex: none; }
  .venue--corvale .venue-photo {
    background: linear-gradient(180deg, #b9d2ea 0%, #6f8a5a 35%, #4f6a34 60%, #3d3f3a 100%);
  }
  .venue--brackenridge .venue-photo {
    background: linear-gradient(180deg, #c7d6e0 0%, #4e6d3a 30%, #6d7a55 50%, #8d8a82 70%, #6c6a66 100%);
  }
  .venue-info {
    flex: 1; padding: 22px 0 0 23px; color: var(--white); overflow: hidden;
  }
  .venue--corvale .venue-info { background: var(--orange); }
  .venue--brackenridge .venue-info { background: var(--green); padding-top: 32px; }
  .venue-name {
    font-weight: 700; font-size: 23px; line-height: 30px; letter-spacing: 0.3px;
  }
  .venue--brackenridge .venue-name { font-size: 19px; letter-spacing: 0; white-space: nowrap; }
  .schedule { margin-top: 10px; color: var(--ink); font-weight: 700; font-size: 20px; line-height: 30px; }
  .venue--brackenridge .schedule { margin-top: 22px; }
  .schedule-row { display: flex; width: 212px; justify-content: space-between; white-space: nowrap; }
  .venue--corvale .schedule-row { width: 190px; }
  .offer {
    position: absolute; left: 53px; top: 510px;
    color: var(--white); font-weight: 700; font-size: 14px; line-height: 19.5px; letter-spacing: 0.3px;
  }
  .price-badge { position: absolute; left: 46px; top: 598px; width: 180px; height: 180px; }
  .price-text {
    position: absolute; left: 46px; top: 640px; width: 180px; text-align: center; color: var(--orange);
    font-weight: 700; line-height: 1;
  }
  .price-amount { display: block; }
  .price-currency { font-size: 44px; vertical-align: 6px; letter-spacing: -2px; }
  .price-value { font-size: 76px; letter-spacing: -3px; }
  .price-unit { display: block; margin-top: 6px; font-size: 11px; color: var(--green); }
  .footer-band {
    position: absolute; left: 0; top: 856px; width: 636px; height: 44px;
    background: var(--night); color: var(--orange);
    font-weight: 700; font-size: 14.5px; text-align: center; line-height: 40px; letter-spacing: 0.2px;
  }
</style>
</head>
<body>
  <main class="flyer">
    <div class="sunset-photo" role="img" aria-label="Photo of two runners silhouetted against an orange sunset sky"></div>

    <h1 class="client-name">Greta Moxley</h1>

    <section class="venue venue--corvale">
      <div class="venue-photo" role="img" aria-label="Photo of the tree-lined grounds at Corvale High School"></div>
      <div class="venue-info">
        <h2 class="venue-name">CORVALE<br>HIGH SCHOOL</h2>
        <div class="schedule">
          <div class="schedule-row"><span>Thursdays</span><span>6.30pm</span></div>
          <div class="schedule-row"><span>Saturdays</span><span>8.00am</span></div>
        </div>
      </div>
    </section>

    <section class="venue venue--brackenridge">
      <div class="venue-photo" role="img" aria-label="Photo of Brackenridge Oval with its clubhouse and bushland"></div>
      <div class="venue-info">
        <h2 class="venue-name">BRACKENRIDGE OVAL</h2>
        <div class="schedule">
          <div class="schedule-row"><span>Wednesdays</span><span>7.30am</span></div>
          <div class="schedule-row"><span>Sundays</span><span>8.00am</span></div>
        </div>
      </div>
    </section>

    <p class="offer">FIRST 5 PEOPLE TO<br>JOIN EITHER GROUP<br>WILL GET FIRST SESSION<br>AT HALF PRICE</p>

    <svg class="price-badge" viewBox="0 0 200 200" aria-hidden="true">
      <polygon fill="var(--night)" points="190,100 167.6,118.1 177.9,145 149.5,149.5 145,177.9 118.1,167.6 100,190 81.9,167.6 55,177.9 50.5,149.5 22.1,145 32.4,118.1 10,100 32.4,81.9 22.1,55 50.5,50.5 55,22.1 81.9,32.4 100,10 118.1,32.4 145,22.1 149.5,50.5 177.9,55 167.6,81.9"/>
    </svg>
    <p class="price-text">
      <span class="price-amount"><span class="price-currency">$</span><span class="price-value">15</span></span>
      <span class="price-unit">PER PERSON</span>
    </p>

    <footer class="footer-band">GROUPS WILL BE FOR UP TO 8 PEOPLE AND ARE FOR ALL FITNESS LEVELS</footer>
  </main>
</body>
</html>
```